Lanterns over lake/list. Wedding planning checklist design

We are a wedding videography start-up that's about to launch a chatterleaf campaign. We need a simple yet premium looking design to showcase a wedding planning checklist which we have written. The main focus of the design should be:

- On A4 pages
- Appeal to young engaged women
- Anyone at home can print it off and stick it onto a fridge
- Premium looking

The contents doesn't have to be on one piece of A4, the list can span more than one page. Also, it doesn't have to be traditional folded brochure style, a full A4 sized list is preferred. The design will potentially be used in further A4 brochure style blog posts. The written checklist and our company logo is attached for reference.

Target Market(s)

Young engaged woman

Industry/Entity Type

Wedding

Requirements
Must have
• Simple and premium feel.
Nice to have
• flexible design that can be reused in the future for blog posts.

```html
<!DOCTYPE html>
<html lang="en">
<head>
<meta charset="utf-8">
<title>Tidewell wedding films — The Ultimate Wedding Planning Checklist</title>
<link href="https://fonts.googleapis.com/css2?family=Didact+Gothic&family=Playball&family=Reenie+Beanie&family=Pinyon+Script&family=Playfair+Display:ital@1&display=swap" rel="stylesheet">
<style>
  :root {
    --peach: #f8bca8;
    --peach-light: #fbcdbc;
    --ink: #262222;
    --body: #3a3434;
    --gold: #c98f3a;
    --white: #ffffff;
  }
  * { box-sizing: border-box; margin: 0; padding: 0; }
  html, body { width: 1200px; height: 848px; overflow: hidden; background: var(--peach); }
  .page {
    position: relative;
    width: 1200px;
    height: 848px;
    background: var(--peach);
    color: var(--body);
    overflow: hidden;
  }
  .ornament {
    position: absolute;
    background: var(--peach-light);
    border-radius: 50%;
  }
  .ornament--swirl-left { left: -60px; top: -70px; width: 250px; height: 200px; }
  .ornament--swirl-right { left: 940px; top: -20px; width: 280px; height: 360px; border-radius: 45%; }
  .ornament--rose { left: -10px; top: 415px; width: 95px; height: 110px; }
  .ornament--tulip { left: 978px; top: 222px; width: 62px; height: 80px; }
  .ornament--swirl-bottom { left: 1050px; top: 720px; width: 200px; height: 160px; }

  .brand {
    position: absolute;
    top: 78px;
    left: 0;
    width: 1200px;
    text-align: center;
    font-family: "Didact Gothic", sans-serif;
    font-size: 34px;
    color: var(--ink);
  }
  .title {
    position: absolute;
    top: 154px;
    left: 0;
    width: 1186px;
    text-align: center;
    font-family: "Playball", cursive;
    font-size: 48px;
    font-weight: 400;
    color: var(--ink);
  }
  .timeline { position: absolute; left: 0; top: 0; }
  .photo {
    position: absolute;
    background: var(--white);
    padding: 7px;
    box-shadow: 2px 4px 10px rgba(90, 40, 30, 0.3);
  }
  .photo__fill { width: 100%; height: 100%; }
  .photo--aisle { left: 92px; top: 322px; width: 180px; height: 128px; transform: rotate(5deg); }
  .photo--aisle .photo__fill { background: linear-gradient(120deg, #c9cdd3, #e7b7c8 55%, #b9bec6); }
  .photo--cake { left: 288px; top: 236px; width: 126px; height: 198px; transform: rotate(-3deg); }
  .photo--cake .photo__fill { background: linear-gradient(180deg, #6f8a5e, #f0d9df 35%, #f3e4e8 80%, #8da070); }
  .photo--couple { left: 484px; top: 244px; width: 170px; height: 118px; transform: rotate(-10deg); }
  .photo--couple .photo__fill { background: linear-gradient(180deg, #dfe0dc, #b9a98b 60%, #a5926d); }
  .photo--favours { left: 680px; top: 312px; width: 146px; height: 110px; transform: rotate(8deg); }
  .photo--favours .photo__fill { background: linear-gradient(135deg, #efe7dd, #c9a27a 55%, #e9ddd0); }

  .handwriting { position: absolute; font-family: "Reenie Beanie", cursive; color: var(--ink); }
  .author { left: 1000px; top: 284px; width: 170px; text-align: center; font-size: 20px; line-height: 24px; }
  .phone { left: 866px; top: 328px; font-size: 25px; transform: rotate(-14deg); letter-spacing: 1px; }
  .email { left: 860px; top: 376px; font-size: 21px; transform: rotate(-20deg); }

  .months { position: absolute; left: 30px; top: 582px; color: var(--gold); text-align: center; width: 130px; }
  .months__number { display: block; font-family: "Playfair Display", serif; font-style: italic; font-size: 112px; line-height: 100px; }
  .months__word { display: block; font-family: "Pinyon Script", cursive; font-size: 38px; line-height: 28px; margin-top: -8px; }

  .checklist { list-style: none; position: absolute; left: 0; top: 0; }
  .task { position: absolute; left: 186px; width: 990px; display: flex; }
  .task__dot { width: 21px; height: 21px; border-radius: 50%; background: var(--white); flex: none; margin-top: 3px; }
  .task__name { font-family: "Didact Gothic", sans-serif; font-size: 21px; line-height: 26px; color: var(--ink); width: 437px; padding-left: 13px; padding-right: 60px; flex: none; }
  .task__note { font-family: "Didact Gothic", sans-serif; font-size: 17px; line-height: 21px; color: var(--body); width: 530px; margin-top: -2px; }
  .task--date { top: 497px; }
  .task--date .task__name { padding-left: 17px; }
  .task--budget { top: 575px; }
  .task--type { top: 662px; }
  .task--party { top: 741px; }
</style>
</head>
<body>
<main class="page">
  <div class="ornament ornament--swirl-left" role="img" aria-label="White flourish swirl ornament"></div>
  <div class="ornament ornament--swirl-right" role="img" aria-label="White ribbon swirl ornament"></div>
  <div class="ornament ornament--rose" role="img" aria-label="White line drawing of a rose"></div>
  <div class="ornament ornament--tulip" role="img" aria-label="White line drawing of a tulip"></div>
  <div class="ornament ornament--swirl-bottom" role="img" aria-label="White flourish swirl ornament"></div>

  <div class="brand">Tidewell wedding films</div>
  <h1 class="title">The Ultimate Wedding Planning Checklist</h1>

  <svg class="timeline" width="1200" height="848" viewBox="0 0 1200 848" aria-hidden="true">
    <path d="M150 345 C220 280 300 240 380 228 C470 214 560 210 640 238 C720 266 780 330 850 360 C900 382 960 378 1000 330"
          fill="none" stroke="#ffffff" stroke-width="3"/>
  </svg>

  <figure class="photo photo--aisle"><div class="photo__fill" role="img" aria-label="Photo of pink flower posies hung along white aisle chairs"></div></figure>
  <figure class="photo photo--cake"><div class="photo__fill" role="img" aria-label="Photo of a tiered white and pink wedding cake in a garden"></div></figure>
  <figure class="photo photo--couple"><div class="photo__fill" role="img" aria-label="Photo of a bride and groom embracing in a field"></div></figure>
  <figure class="photo photo--favours"><div class="photo__fill" role="img" aria-label="Photo of lace-wrapped wedding favour boxes"></div></figure>

  <p class="handwriting author">Written by Nora Vell<br>Wedding Planner</p>
  <p class="handwriting phone">0219470612</p>
  <p class="handwriting email">noravell4@postbox.com</p>

  <div class="months"><span class="months__number">12</span><span class="months__word">months</span></div>

  <ul class="checklist">
    <li class="task task--date"><span class="task__dot"></span><span class="task__name">Decide on a date and venue</span><span class="task__note">The earlier you can reserve these, the better! Will it be a church garden or beach&nbsp; wedding?</span></li>
    <li class="task task--budget"><span class="task__dot"></span><span class="task__name">Organise a meeting of the parents and determine your budget</span><span class="task__note">Work out how much each family is contributing so that there are no surprises</span></li>
    <li class="task task--type"><span class="task__dot"></span><span class="task__name">Choose the type of wedding</span><span class="task__note">Form a basic idea of the kind of wedding you would like to have e.g.- simple or lavish?</span></li>
    <li class="task task--party"><span class="task__dot"></span><span class="task__name">Pick your wedding party</span><span class="task__note">Best man, groomsmen, maid of honor, bridesmaids, flower girl, ring bearer etc.</span></li>
  </ul>
</main>
</body>
</html>
```